Create a memorable Stationary for Security Software Company

TalbrenQuay is the worldwide leader in securing the Internet. Making Internet communications and critical data secure, reliable and available everywhere has been and continues to be our ongoing vision. We are committed to staying focused on real customer needs and to developing new and innovative security solutions that redefine the security landscape.

Industry/Entity Type

Internet

Font styles to use
Serif
Sans Serif
Script

Colors
0792cd
33a6d7
85cae6

```html
<!DOCTYPE html>
<html lang="en">
<head>
<meta charset="utf-8">
<title>TalbrenQuay Business Card</title>
<link rel="stylesheet" href="https://fonts.googleapis.com/css2?family=Source+Sans+3:wght@400;600;700&display=swap">
<style>
  :root {
    --backdrop: #8e8e8e;
    --front-face: #74b3d6;
    --front-border: #3f9acb;
    --back-face: #2b8dc2;
    --ink-strong: #1d6f9f;
    --ink-body: #3a6680;
    --ink-mark: #2f86b8;
    --ink-back: #1f78a9;
    --rule: #4a8fb7;
  }
  * { box-sizing: border-box; margin: 0; padding: 0; }
  html, body {
    width: 1105px; height: 1200px; overflow: hidden;
    background: var(--backdrop);
    font-family: "Source Sans 3", sans-serif;
  }
  .card {
    position: absolute; left: 182px; width: 748px; height: 426px;
    overflow: hidden;
  }
  .card--front { top: 119px; background: var(--front-border); }
  .card--back { top: 637px; background: var(--back-face); }

  .front-border { position: absolute; inset: 0; }
  .front-panel {
    position: absolute; left: 36px; top: 30px; right: 36px; bottom: 32px;
    background: var(--front-face); border-radius: 26px;
  }

  .brand-mark {
    position: absolute; left: 100px; top: 180px;
    display: flex; align-items: center; gap: 10px;
    font-weight: 700; font-size: 31px; color: var(--ink-mark);
  }
  .brand-mark .dot {
    width: 22px; height: 22px; border-radius: 50%; background: var(--ink-mark);
  }

  .divider {
    position: absolute; left: 371px; top: 88px; width: 1px; height: 250px;
    background: var(--rule);
  }

  .details { position: absolute; left: 406px; top: 92px; color: var(--ink-body); }
  .person-name { font-size: 26px; font-weight: 700; color: var(--ink-strong); line-height: 1.2; }
  .person-role { font-size: 20px; line-height: 1.3; margin-bottom: 14px; }
  .address { font-size: 19px; line-height: 28px; margin-bottom: 12px; }
  .contact-list { list-style: none; }
  .contact-list li {
    display: flex; align-items: center; gap: 12px;
    font-size: 19px; line-height: 29px;
  }
  .contact-list svg { width: 17px; height: 17px; fill: var(--ink-strong); flex: none; }

  .back-mark {
    position: absolute; left: 0; right: 0; top: 150px;
    display: flex; flex-direction: column; align-items: center; gap: 14px;
    font-weight: 700; font-size: 34px; color: var(--ink-back);
  }
  .back-mark .dot {
    width: 70px; height: 70px; border-radius: 50%; background: #2682b5;
  }
  .back-url {
    position: absolute; left: 0; right: 0; top: 355px; text-align: center;
    font-size: 19px; letter-spacing: 9px; color: var(--ink-back);
  }
</style>
</head>
<body>
  <section class="card card--front">
    <svg class="front-border" role="img" aria-label="Decorative cloud border framing the card" width="748" height="426">
      <rect width="748" height="426" fill="var(--front-border)"/>
    </svg>
    <div class="front-panel"></div>

    <div class="brand-mark"><span class="dot"></span>TalbrenQuay</div>

    <div class="divider"></div>

    <div class="details">
      <p class="person-name">Idris Calloway</p>
      <p class="person-role">CEO/Founder</p>
      <p class="address">4120 Larkspur Row<br>Juneau, Alaska 99801</p>
      <ul class="contact-list">
        <li>
          <svg viewBox="0 0 24 24"><path d="M6.6 10.8a15.1 15.1 0 0 0 6.6 6.6l2.2-2.2c.3-.3.7-.4 1-.2 1.1.4 2.3.6 3.6.6.6 0 1 .4 1 1V20c0 .6-.4 1-1 1A17 17 0 0 1 3 4c0-.6.4-1 1-1h3.5c.6 0 1 .4 1 1 0 1.3.2 2.5.6 3.6.1.3 0 .7-.2 1z"/></svg>
          907 512 3846
        </li>
        <li>
          <svg viewBox="0 0 24 24"><path d="M6 3h12v5H6zM3 9h18v8h-3v4H6v-4H3zm5 6v4h8v-4z"/></svg>
          907 512 3847
        </li>
        <li>
          <svg viewBox="0 0 24 24"><path d="M2 5h20v14H2zm2 2v.5l8 5 8-5V7z"/></svg>
          hello@talbrenquay.com
        </li>
        <li>
          <svg viewBox="0 0 24 24"><path d="M12 2a10 10 0 1 0 0 20 10 10 0 0 0 0-20zm0 2a8 8 0 0 1 7.4 5H15c-.5-2-1.5-3.8-3-5zm-2.6.4C8 6 7.2 7.5 7 9H4.6a8 8 0 0 1 4.8-4.6zM4.2 11H7v2H4.2zm.4 4H7c.3 1.6 1 3.1 2.4 4.6A8 8 0 0 1 4.6 15zM9 11h6v2H9zm.1 4h5.8c-.5 1.9-1.5 3.4-2.9 4.7-1.4-1.3-2.4-2.8-2.9-4.7zM17 11h2.8v2H17zm0 4h2.4a8 8 0 0 1-4.8 4.6c1.4-1.5 2.1-3 2.4-4.6zM9.1 9c.5-1.9 1.5-3.4 2.9-4.7 1.4 1.3 2.4 2.8 2.9 4.7z"/></svg>
          www.talbrenquay.com
        </li>
      </ul>
    </div>
  </section>

  <section class="card card--back">
    <div class="back-mark"><span class="dot"></span>TalbrenQuay</div>
    <p class="back-url">www.talbrenquay.com</p>
  </section>
</body>
</html>
```